Präsentationsvorlagen für Strahlenschutzkurse
Zielgruppe
Wir bieten Strahlenschutzkurse in der Medizin an. Zielgruppe: Ärztinnen und Ärzte
Stichworte: Erwachsenenbildung, wissenschaftliche Inhalte
Aufgabenstellung
Wir benötigen eine Power-Point Präsentationsvorlage für unsere Kurse.
Auf allen Folien:
*Integration von unserem Logo
*Übernahme unseres bestehenden Farbkonzepts
*Feld für Überschrift
*kleines Textfeld für die Angabe der jeweiligen Quelle
Wir benötigen:
eine Folie nur mit Textfeld (z.B. Aufzählung, kurzer Text)
eine Folie Text mit Bild
eine Folie Bild bzw. Video
eine Folie mit einem wichtigen Lehrinhalt (wichtiger Text) - besondere Vorhebung erwünscht
eine Folie für Anfang bzw. Ende
HEX-CODE:
#4f93fe
#eea62f
#ffffff

```html
<!DOCTYPE html>
<html lang="de">
<head>
<meta charset="utf-8">
<title>Folie Text mit Bild</title>
<link rel="stylesheet" href="https://fonts.googleapis.com/css2?family=Open+Sans:wght@300;400;600&display=swap">
<style>
  :root {
    --navy: #3b5b85;
    --ink: #111111;
    --media: #4472c4;
    --footer: #9ca7b5;
    --paper: #ffffff;
    --haze: #e6e9ee;
  }
  * { margin: 0; padding: 0; box-sizing: border-box; }
  html, body { width: 1200px; height: 675px; overflow: hidden; background: var(--paper); }
  .slide {
    position: relative;
    width: 1200px;
    height: 675px;
    overflow: hidden;
    font-family: "Open Sans", Arial, sans-serif;
    background: linear-gradient(to bottom, var(--paper) 0, var(--paper) 390px, var(--haze) 564px);
  }
  .slide-title {
    position: absolute;
    left: 161px;
    top: 104px;
    font-weight: 300;
    font-size: 43px;
    line-height: 1.2;
    color: var(--navy);
    letter-spacing: -0.2px;
  }
  .brand-corner {
    position: absolute;
    left: 1040px;
    top: 34px;
    width: 124px;
    display: flex;
    flex-direction: column;
    align-items: center;
    gap: 8px;
    color: var(--navy);
    font-size: 12px;
    font-weight: 400;
    text-align: center;
    line-height: 1.25;
  }
  .brand-corner .brand-dot {
    width: 84px;
    height: 84px;
    border-radius: 50%;
    border: 5px solid var(--navy);
  }
  .body-text {
    position: absolute;
    left: 161px;
    top: 187px;
    width: 490px;
    font-size: 23.5px;
    line-height: 33px;
    color: var(--ink);
  }
  .body-text p + p { margin-top: 58px; }
  .media-placeholder {
    position: absolute;
    left: 680px;
    top: 195px;
    width: 370px;
    height: 299px;
    background: var(--media);
  }
  .footer-band {
    position: absolute;
    left: 0;
    top: 564px;
    width: 1200px;
    height: 111px;
    background: var(--footer);
    color: var(--paper);
  }
  .footer-brand {
    position: absolute;
    left: 30px;
    top: 34px;
    display: flex;
    align-items: center;
    gap: 10px;
    font-size: 11px;
    font-weight: 400;
    line-height: 1.3;
  }
  .footer-brand .brand-dot {
    width: 38px;
    height: 38px;
    border-radius: 50%;
    border: 2px solid var(--paper);
  }
  .source-field {
    position: absolute;
    left: 867px;
    top: 47px;
    font-size: 18px;
  }
  .page-number {
    position: absolute;
    left: 1140px;
    top: 50px;
    font-size: 14px;
  }
</style>
</head>
<body>
<div class="slide">
  <h1 class="slide-title">Überschrift Folie Text mit Bild</h1>

  <div class="brand-corner">
    <span class="brand-dot"></span>
    <span>Dr. Lindqvist &amp; Morawe Strahlenschutz</span>
  </div>

  <div class="body-text">
    <p>Lorem ipsum dolor sit amet, consetetur sadipscing elitr, sed diam nonumy eirmod tempor invidunt ut labore et dolore magna aliquyam erat, sed diam voluptua.</p>
    <p>Lorem ipsum dolor sit amet, consetetur sadipscing elitr.</p>
  </div>

  <div class="media-placeholder" role="img" aria-label="Platzhalter für ein Bild zum Lehrinhalt"></div>

  <footer class="footer-band">
    <div class="footer-brand">
      <span class="brand-dot"></span>
      <span>Dr. Lindqvist &amp; Morawe<br>Strahlenschutz</span>
    </div>
    <div class="source-field">Feld Quellangaben</div>
    <div class="page-number">4</div>
  </footer>
</div>
</body>
</html>
```